KVT Website (Halcyon Guard Networks)

We need a web design for an established company in Dubai, U.A.E, called Halcyon Guard Network. We provide a completed solutions in ICT-Information and Communication Technology (Computer, Networking, IP Telephony, Software and Hardware) and Security Systems (CCTV, Access Control, and System Integrator), our Services include Consultancy Planning and Design, Value Added Distribution, Implementation and Execution, Operations and Maintenance, Training and Development. We help our Clients to Develop and Secure their infrastructure. We would like to see design that use our logo theme, reflect our solutions and services, communicate to enterprise Technology and Security. Website must be responsive, Dynamic, symmetry or asymmetry or both.
Regards,

Target Market(s)

UAE

Industry/Entity Type

It Company

Coding

Coded - Design and coding required

Number of Pages Required

5+ page

Font styles to use
Sans Serif

Requirements
Must have
• Logo Theme, social media logos and links,
Nice to have
• Big blogs and banners
Should not have
• Many colors or congested design

```html
<!DOCTYPE html>
<html lang="en">
<head>
<meta charset="utf-8">
<title>Halcyon Guard Networks</title>
<link rel="stylesheet" href="https://fonts.googleapis.com/css2?family=Open+Sans:wght@300;400;600;700&display=swap">
<style>
  :root {
    --gold: #e2b93b;
    --gold-dark: #c99e22;
    --charcoal: #2b2b2b;
    --charcoal-deep: #1f1f1f;
    --nav-grey: #3a3a3a;
    --text-dark: #222222;
    --text-body: #666666;
    --white: #ffffff;
  }
  * { box-sizing: border-box; margin: 0; padding: 0; }
  html, body { width: 755px; height: 1200px; overflow: hidden; }
  body { font-family: "Open Sans", Arial, sans-serif; background: var(--white); color: var(--text-dark); }
  .page { width: 755px; height: 1200px; position: relative; }
  .container { width: 670px; margin: 0 auto; position: relative; }

  /* Header */
  .site-header {
    height: 113px;
    background: linear-gradient(#3a3a3a, #262626);
    border-top: 4px solid var(--gold);
    position: relative;
  }
  .brand {
    position: absolute; left: 45px; top: 16px;
    color: var(--gold); font-weight: 600; font-size: 15px; line-height: 18px;
    width: 120px;
  }
  .main-nav {
    position: absolute; left: 42px; right: 42px; top: 74px; height: 35px;
    display: flex; background: var(--nav-grey);
  }
  .main-nav a {
    flex: 1; display: flex; align-items: center; justify-content: center;
    color: var(--white); text-decoration: none; font-size: 10px;
    border-right: 1px solid #2a2a2a;
  }
  .main-nav a:last-child { border-right: 0; }
  .main-nav a.active { background: var(--gold); color: var(--text-dark); flex: 0.8; }
  .main-nav a.wide { flex: 1.3; }

  /* Hero */
  .hero { height: 360px; position: relative; overflow: hidden; }
  .hero-photo {
    position: absolute; inset: 0;
    background: radial-gradient(ellipse at 28% 40%, #8a8a8a 0%, #5a5a5a 35%, #2e2e2e 75%, #1c1c1c 100%);
  }
  .hero-tagline {
    position: absolute; left: 365px; top: 125px; width: 350px;
    color: var(--white); font-weight: 400; font-size: 18px; line-height: 26px;
  }
  .hero-tagline .big { font-size: 24px; }
  .hero-dots { position: absolute; right: 50px; top: 238px; display: flex; gap: 5px; }
  .hero-dots span { width: 7px; height: 7px; border-radius: 50%; background: #9a9a9a; }
  .hero-dots span.on { background: var(--gold); }

  /* Headings */
  .section-title { text-align: center; font-weight: 700; font-size: 21px; color: var(--text-dark); }
  .section-title .accent { color: var(--gold); }

  /* About */
  .about { height: 187px; padding-top: 20px; text-align: center; }
  .about p {
    margin-top: 14px; font-size: 7.5px; line-height: 12px; color: var(--text-body); text-align: center;
  }
  .btn {
    display: inline-block; background: var(--gold); color: var(--text-dark);
    text-decoration: none; font-size: 8px;
  }
  .about .btn { margin-top: 16px; width: 88px; height: 22px; line-height: 22px; }

  /* Services */
  .services { height: 276px; position: relative; overflow: hidden; }
  .services-photo {
    position: absolute; inset: 0;
    background: linear-gradient(160deg, #4a4a4a 0%, #2f2f2f 45%, #3b3b3b 70%, #222 100%);
  }
  .services .section-title { position: relative; color: var(--white); padding-top: 46px; font-size: 20px; }
  .service-grid { position: relative; display: flex; justify-content: space-between; margin-top: 18px; }
  .service { width: 190px; text-align: center; color: var(--white); }
  .service-icon {
    width: 46px; height: 46px; border-radius: 50%; background: var(--gold);
    margin: 0 auto; display: flex; align-items: center; justify-content: center;
  }
  .service h3 { margin-top: 12px; font-size: 10px; font-weight: 400; letter-spacing: .3px; }
  .service p { margin-top: 7px; font-size: 7px; line-height: 10px; color: #cfcfcf; }
  .service .btn { margin-top: 26px; width: 55px; height: 14px; line-height: 14px; font-size: 6.5px; }

  /* Projects */
  .projects { height: 184px; padding-top: 42px; }
  .projects .section-title { font-size: 20px; }
  .carousel-arrows { position: absolute; right: 4px; top: 4px; display: flex; gap: 10px; }
  .project-row { display: flex; justify-content: space-between; margin-top: 18px; }
  .project-thumb { width: 126px; height: 88px; }
  .thumb-a { background: linear-gradient(135deg, #cfe3f2, #6f8ea8); }
  .thumb-b { background: linear-gradient(135deg, #e8eef5, #4b6f96); }
  .thumb-c { background: linear-gradient(135deg, #5aa4e0, #1c4f8c); }
  .thumb-d { background: linear-gradient(135deg, #dde7f0, #8aa1b7); }
  .thumb-e { background: linear-gradient(135deg, #f1f1ec, #b7bcc0); }

  /* Footer */
  .site-footer { height: 80px; background: var(--charcoal-deep); position: relative; }
  .copyright { position: absolute; left: 45px; top: 34px; color: #bdbdbd; font-size: 7.5px; }
  .social-links { position: absolute; right: 45px; top: 29px; display: flex; gap: 5px; }
  .social-links a { width: 17px; height: 17px; border-radius: 50%; background: var(--white); display: block; }
</style>
</head>
<body>
<div class="page">

  <header class="site-header">
    <div class="brand">Halcyon Guard Networks</div>
    <nav class="main-nav">
      <a href="#" class="active">Home</a>
      <a href="#">About us</a>
      <a href="#" class="wide">Specialized Projects</a>
      <a href="#" class="wide">Business Intelligence</a>
      <a href="#">Contact us</a>
    </nav>
  </header>

  <section class="hero">
    <div class="hero-photo" role="img" aria-label="Black and white photo of a CCTV security camera mounted on a wall"></div>
    <h1 class="hero-tagline">A company which provides security design, including <span class="big">CCTV</span> and other electronic design</h1>
    <div class="hero-dots"><span class="on"></span><span></span><span></span></div>
  </section>

  <section class="about">
    <div class="container">
      <h2 class="section-title">About <span class="accent">Us</span></h2>
      <p>We deliver complete solutions in information and communication technology, from computer networks and IP telephony to software and hardware. Our security systems cover CCTV, access control and full system integration for offices, towers and industrial sites across the region. Our team guides every project through consultancy, planning and design, then carries it through distribution, implementation and execution. After handover we stay on with operations, maintenance, training and development, so your staff can run every system with confidence. We help our clients develop and secure their infrastructure with proven products and a careful, friendly service.</p>
      <a href="#" class="btn">Read More</a>
    </div>
  </section>

  <section class="services">
    <div class="services-photo" role="img" aria-label="Dark photo of modern office buildings behind glass"></div>
    <h2 class="section-title">Featured Services</h2>
    <div class="container service-grid">
      <div class="service">
        <div class="service-icon">
          <svg width="20" height="22" viewBox="0 0 20 22"><path d="M10 1 L18 4 V10 C18 15 14.5 19 10 21 C5.5 19 2 15 2 10 V4 Z" fill="#2b2b2b"/><path d="M10 4 V18 C6.8 16.5 5 13.5 5 10 V6 Z" fill="#e2b93b"/></svg>
        </div>
        <h3>ESTIBULUM VEL</h3>
        <p>Consultancy, planning and design for secure networks, tailored to each site and budget.</p>
        <a href="#" class="btn">MORE</a>
      </div>
      <div class="service">
        <div class="service-icon">
          <svg width="20" height="22" viewBox="0 0 20 22"><circle cx="10" cy="6.5" r="4.5" fill="#2b2b2b"/><path d="M2 21 C2 15 5.5 12 10 12 C14.5 12 18 15 18 21 Z" fill="#2b2b2b"/></svg>
        </div>
        <h3>ESTIBULUM VEL</h3>
        <p>Implementation and execution by skilled engineers, on time and to the agreed plan.</p>
        <a href="#" class="btn">MORE</a>
      </div>
      <div class="service">
        <div class="service-icon">
          <svg width="20" height="22" viewBox="0 0 20 22"><path d="M5 10 V6.5 C5 3.5 7.2 1.5 10 1.5 C12.8 1.5 15 3.5 15 6.5 V8" fill="none" stroke="#2b2b2b" stroke-width="2.4"/><rect x="3" y="10" width="14" height="11" rx="1.5" fill="#2b2b2b"/><circle cx="10" cy="15" r="1.8" fill="#e2b93b"/></svg>
        </div>
        <h3>ESTIBULUM VEL</h3>
        <p>Operations, maintenance and training that keep every system running year after year.</p>
        <a href="#" class="btn">MORE</a>
      </div>
    </div>
  </section>

  <section class="projects">
    <div class="container">
      <h2 class="section-title">Specialized <span class="accent">Projects</span></h2>
      <div class="carousel-arrows">
        <svg width="10" height="10" viewBox="0 0 10 10"><path d="M9 5 H1 M4 2 L1 5 L4 8" stroke="#222" stroke-width="1.6" fill="none"/></svg>
        <svg width="10" height="10" viewBox="0 0 10 10"><path d="M1 5 H9 M6 2 L9 5 L6 8" stroke="#222" stroke-width="1.6" fill="none"/></svg>
      </div>
      <div class="project-row">
        <div class="project-thumb thumb-a" role="img" aria-label="Photo of security cameras on a building corner"></div>
        <div class="project-thumb thumb-b" role="img" aria-label="Photo of an access control keypad at a door"></div>
        <div class="project-thumb thumb-c" role="img" aria-label="Photo of a wall of surveillance monitors"></div>
        <div class="project-thumb thumb-d" role="img" aria-label="Photo of a dome camera on a ceiling"></div>
        <div class="project-thumb thumb-e" role="img" aria-label="Photo of an outdoor bullet camera"></div>
      </div>
    </div>
  </section>

  <footer class="site-footer">
    <p class="copyright">Copyright © 2015. Yoursite. All Right Reserved</p>
    <div class="social-links">
      <a href="#" aria-label="Social link"></a>
      <a href="#" aria-label="Social link"></a>
      <a href="#" aria-label="Social link"></a>
      <a href="#" aria-label="Social link"></a>
      <a href="#" aria-label="Social link"></a>
    </div>
  </footer>

</div>
</body>
</html>
```